electric fence manufacturer needs a international catalogue

our company "valmire systems co.,ltd" is base on shenzhen China.
our product is electric fence system. including the energiser and accesories.
our system seperated into 2 section.
1.perimeter security product, pls check attachment for the project picture. we use the high voltage pulse to stop the intruder and bad man. once we touch the wire , you will get shock. but it is safe, just make you unconfortable.
2.farm electric fencing. to keep the animal inside or outside. the same function with security system.
we prefer color such as green. orange.
we want to express is our life is getting peace and comfortable and relax and easy by using electric fencing
3. page size A4

Target Market(s)

global market ,

Industry/Entity Type

Security

```html
<!DOCTYPE html>
<html lang="en">
<head>
<meta charset="utf-8">
<title>Valmire Systems — Catalogue Back Cover</title>
<link href="https://fonts.googleapis.com/css2?family=Arimo:wght@400;700&display=swap" rel="stylesheet">
<style>
  :root {
    --sky-top: #e4e7ea;
    --sky-low: #d3d8dc;
    --horse: #6a5448;
    --pasture: #7f8f5a;
    --green-light: #a6d046;
    --green-mid: #6ea544;
    --green-deep: #2f7048;
    --orange-warm: #f5922a;
    --orange-sun: #fcc72a;
    --text-light: #ffffff;
  }
  * { margin: 0; padding: 0; box-sizing: border-box; }
  html, body {
    width: 849px;
    height: 1200px;
    overflow: hidden;
    background: #ffffff;
  }
  .back-cover {
    position: relative;
    width: 849px;
    height: 1200px;
    overflow: hidden;
  }
  .pasture-photo {
    position: absolute;
    inset: 0;
    background:
      radial-gradient(ellipse 55% 22% at 35% 42%, var(--horse) 0%, rgba(106,84,72,0.55) 55%, rgba(106,84,72,0) 100%),
      linear-gradient(180deg, var(--sky-top) 0%, var(--sky-low) 30%, #c9c4bc 42%, #9d9482 55%, var(--pasture) 75%, #8e9c6c 100%);
  }
  .brand-shapes {
    position: absolute;
    inset: 0;
    width: 849px;
    height: 1200px;
  }
  .company-contact {
    position: absolute;
    left: 141px;
    top: 1025px;
    color: var(--text-light);
    font-family: "Arimo", Arial, sans-serif;
    font-size: 15.5px;
    line-height: 19px;
  }
  .company-name,
  .company-web {
    font-weight: 700;
  }
</style>
</head>
<body>
  <main class="back-cover">
    <div class="pasture-photo" role="img" aria-label="Photo of a horse grazing in a pasture behind a yellow polyrope electric fence wire joined to a coiled gate spring, under a pale cloudy sky"></div>

    <svg class="brand-shapes" viewBox="0 0 849 1200" aria-hidden="true">
      <defs>
        <radialGradient id="bolt-green" cx="420" cy="620" r="520" gradientUnits="userSpaceOnUse">
          <stop offset="0" stop-color="var(--green-light)"/>
          <stop offset="0.5" stop-color="var(--green-mid)"/>
          <stop offset="1" stop-color="var(--green-deep)"/>
        </radialGradient>
        <radialGradient id="field-orange" cx="520" cy="980" r="620" gradientUnits="userSpaceOnUse">
          <stop offset="0" stop-color="var(--orange-sun)"/>
          <stop offset="0.55" stop-color="#fbbd2a"/>
          <stop offset="1" stop-color="var(--orange-warm)"/>
        </radialGradient>
      </defs>
      <polygon class="bolt-band" fill="url(#bolt-green)"
        points="0,1078 360,440 478,656 849,304 849,1200 0,1200"/>
      <polygon class="field-block" fill="url(#field-orange)"
        points="0,1114 365,762 485,966 849,333 849,1200 0,1200"/>
    </svg>

    <address class="company-contact">
      <div class="company-name">Valmire Systems Co.,Ltd</div>
      <div>Add: Unit 1207, Qinghe Tower, Meilan Rd, Bao'an District,</div>
      <div>Shenzhen City, Guangdong, China, 518100</div>
      <div>Sales: leo@valmiresys.com | mia@valmiresys.com</div>
      <div class="company-web">www.valmiresys.com</div>
    </address>
  </main>
</body>
</html>
```